Business Card Design and Logo Needed

I need Business Cards and a Logo for my website and public speaking business which can be found at: www.talia-ferrow.com

I'm looking for creative and unique ideas. Some business cards I've found online that I like can be found at:
http://gigmarketloft.com/general/18-smokin-hot-business-card-designs/

and at

http://www.theprintnookery.com/2009/04/50-creative-business-cards-of-50-graphic-designers/

```html
<!DOCTYPE html>
<html lang="en">
<head>
<meta charset="utf-8">
<title>Talia Ferrow – Business Card</title>
<link rel="stylesheet" href="https://fonts.googleapis.com/css2?family=Crimson+Text:ital,wght@0,400;0,700;1,400;1,700&display=swap">
<style>
  :root {
    --page-bg: #ffffff;
    --parchment-light: #f6f1e0;
    --parchment-mid: #e9dcb8;
    --parchment-edge: #a8855a;
    --wood-dark: #4a2a18;
    --brand-red: #8e1c1f;
    --ink: #2a1a14;
    --rule-gold: #b39a5a;
    --back-red: #7a1418;
    --back-deep: #2e0607;
    --mark-grey: rgba(200, 200, 205, 0.72);
  }
  * { margin: 0; padding: 0; box-sizing: border-box; }
  html, body {
    width: 1200px; height: 900px; overflow: hidden;
    background: var(--page-bg);
  }
  body {
    position: relative;
    font-family: "Crimson Text", Georgia, serif;
  }

  .card {
    position: absolute;
    overflow: hidden;
  }
  .card-front { left: 284px; top: 44px; width: 696px; height: 388px; }
  .card-back  { left: 280px; top: 454px; width: 702px; height: 388px; }

  .front-texture {
    position: absolute; inset: 0;
    background:
      radial-gradient(ellipse at 50% 45%, var(--parchment-light) 0%, var(--parchment-light) 45%, var(--parchment-mid) 78%, var(--parchment-edge) 100%);
    box-shadow: inset 14px 0 18px -6px var(--wood-dark), inset -14px 0 18px -6px var(--wood-dark),
                inset 0 10px 14px -8px var(--wood-dark);
  }

  .brand-mark {
    position: absolute; left: 0; right: 0; top: 100px;
    display: flex; justify-content: center; align-items: center; gap: 14px;
  }
  .brand-mark-dot {
    width: 22px; height: 22px; border-radius: 50%;
    background: var(--brand-red);
  }
  .brand-mark-name {
    font-weight: 700; font-size: 46px; line-height: 1;
    color: var(--brand-red);
  }

  .identity {
    position: absolute; left: 0; right: 0; top: 234px;
    text-align: center;
  }
  .identity-name {
    font-weight: 700; font-style: italic; font-size: 32px; line-height: 32px;
    color: var(--brand-red);
  }
  .identity-role {
    font-style: italic; font-size: 22px; line-height: 24px;
    color: var(--brand-red);
  }

  .divider {
    position: absolute; left: 122px; top: 299px; width: 454px; height: 6px;
  }

  .contact {
    position: absolute; left: 0; right: 0; top: 314px;
    text-align: center; font-size: 19px; line-height: 22px; color: var(--ink);
  }
  .contact-label { font-weight: 700; color: var(--brand-red); }
  .contact-item { margin: 0 2px; }

  .back-texture {
    position: absolute; inset: 0;
    background: linear-gradient(120deg, var(--back-deep) 0%, var(--back-red) 30%, var(--back-deep) 55%, var(--back-red) 80%, var(--back-deep) 100%);
  }
  .back-mark {
    position: absolute; inset: 0;
    display: flex; justify-content: center; align-items: center; gap: 18px;
  }
  .back-mark-name {
    font-weight: 700; font-size: 68px; line-height: 1;
    color: var(--mark-grey);
  }
  .back-mark-dot {
    width: 34px; height: 34px; border-radius: 50%;
    background: var(--mark-grey);
  }
</style>
</head>
<body>

<section class="card card-front">
  <div class="front-texture" role="img" aria-label="Aged parchment texture framed by dark wood edges"></div>

  <div class="brand-mark">
    <span class="brand-mark-dot"></span>
    <span class="brand-mark-name">Talia Ferrow</span>
  </div>

  <div class="identity">
    <h1 class="identity-name">Talia Ferrow</h1>
    <p class="identity-role">Speaker, Philanthropist, and Author</p>
  </div>

  <svg class="divider" viewBox="0 0 454 6" aria-hidden="true">
    <line x1="3" y1="3" x2="451" y2="3" stroke="var(--rule-gold)" stroke-width="1.4"/>
    <circle cx="3" cy="3" r="2.6" fill="var(--rule-gold)"/>
    <circle cx="451" cy="3" r="2.6" fill="var(--rule-gold)"/>
  </svg>

  <div class="contact">
    <p>
      <span class="contact-item"><span class="contact-label">mobile:</span> 0400 000 000</span>
      <span class="contact-item"><span class="contact-label">email:</span> talia@talia-ferrow.com</span>
    </p>
    <p><span class="contact-label">website:</span> talia-ferrow.com</p>
  </div>
</section>

<section class="card card-back">
  <div class="back-texture" role="img" aria-label="Deep red wood grain texture running diagonally"></div>
  <div class="back-mark">
    <span class="back-mark-dot"></span>
    <span class="back-mark-name">Talia Ferrow</span>
  </div>
</section>

</body>
</html>
```